Lumo4Kart - a fintech company - business card

We need a business card design for our Payments Technology company in Sydney, Australia. We provide business with payment solutions expanding across EFTPOS machines, online payment gateways and mobile payment solutions. We would like to see designs that are clean, classy and professional.
Target Market(s)
Business professionals, executives, c-suite
Industry/Entity Type
Fintech
Contact Information for Business Card
Will be on 400gsm. Logo will most likely be spot gloss unless designer recommends otherwise.
Font styles to use
Sans Serif
Requirements
Must have
- We need our website (lumo4kart.com.au), email (contact@lumo4kart.com.au), mobile (0432 587 904) and direct phone number (02 6815 3927) to feature on the card along with our logo (attached) and the words "EFTPOS | ONLINE | MOBILE"
- Font = Roboto

```html
<!DOCTYPE html>
<html lang="en">
<head>
<meta charset="utf-8">
<title>Lumo4Kart Business Card</title>
<link rel="stylesheet" href="https://fonts.googleapis.com/css2?family=Roboto:wght@400;700&display=swap">
<style>
  :root {
    --ink-blue: #1c5f8e;
    --mark-blue: #155f91;
    --circle-blue: #3a87bd;
    --teal: #2ec7b0;
    --arc-blue: #3a6fb5;
    --logo-grey: #66676b;
    --card-edge: #222;
    --white: #fff;
  }
  * { margin: 0; padding: 0; box-sizing: border-box; }
  html, body {
    width: 1017px; height: 1200px; overflow: hidden;
    background: var(--white);
    font-family: "Roboto", sans-serif;
  }
  .sheet { position: relative; width: 1017px; height: 1200px; }
  .card {
    position: absolute; left: 1px; width: 1014px; height: 578px;
    border: 1.5px solid var(--card-edge); border-radius: 60px;
    overflow: hidden; background: var(--white);
  }
  .card--front { top: 1px; }
  .card--back { top: 619px; }
  .card svg.shapes { position: absolute; inset: 0; }
  .text { position: absolute; line-height: 1; white-space: nowrap; }
  .brand-name {
    font-weight: 700; color: var(--logo-grey);
    transform: translateX(-50%); letter-spacing: 0.5px;
  }
  .card--front .brand-name { left: 508px; top: 263px; font-size: 72px; }
  .card--back .brand-name { left: 192px; top: 334px; font-size: 48px; }
  .tagline {
    left: 0; right: 0; text-align: center;
    top: 453px; font-size: 32px; letter-spacing: 6.5px; color: var(--ink-blue);
  }
  .address {
    left: 0; right: 0; text-align: center;
    top: 517px; font-size: 30px; letter-spacing: 4.5px; color: var(--ink-blue);
  }
  .contact { color: var(--white); left: 525px; }
  .person-name { top: 101px; font-size: 52px; letter-spacing: 4.5px; }
  .person-role { top: 161px; font-size: 32px; }
  .phone-direct { top: 247px; font-size: 31px; }
  .phone-mobile { top: 299px; font-size: 31px; }
  .email { top: 391px; font-size: 31px; }
  .website { top: 448px; font-size: 31px; }
</style>
</head>
<body>
<main class="sheet">
  <section class="card card--front" aria-label="Card front">
    <svg class="shapes" width="1014" height="578" viewBox="0 0 1014 578">
      <circle class="brand-dot" cx="507" cy="168" r="66" fill="var(--mark-blue)"/>
      <path d="M0 262 Q507 530 1014 262" fill="none" stroke="var(--arc-blue)" stroke-width="6"/>
      <path d="M0 255 Q507 523 1014 255" fill="none" stroke="var(--teal)" stroke-width="6"/>
    </svg>
    <div class="text brand-name">LUMO4KART</div>
    <p class="text tagline">EFTPOS | ONLINE | MOBILE</p>
    <p class="text address">27 Kestrel Row, Wattle Bay VIC 3987, Australia</p>
  </section>

  <section class="card card--back" aria-label="Card back">
    <svg class="shapes" width="1014" height="578" viewBox="0 0 1014 578">
      <circle class="brand-dot" cx="192" cy="252" r="56" fill="var(--mark-blue)"/>
      <circle cx="674" cy="289" r="312" fill="var(--teal)"/>
      <circle cx="702" cy="289" r="312" fill="var(--circle-blue)"/>
      <line x1="525" y1="216" x2="1014" y2="216" stroke="var(--white)" stroke-width="4"/>
      <line x1="525" y1="361" x2="1014" y2="361" stroke="var(--white)" stroke-width="4"/>
    </svg>
    <div class="text brand-name">LUMO4KART</div>
    <p class="text contact person-name">Your Name</p>
    <p class="text contact person-role">Position</p>
    <p class="text contact phone-direct">02 6815 3927</p>
    <p class="text contact phone-mobile">0432 587 904</p>
    <p class="text contact email">contact@lumo4kart.com.au</p>
    <p class="text contact website">www.lumo4kart.com.au</p>
  </section>
</main>
</body>
</html>
```